Brimlow Oakville Cabernet Sauvignon-Wine label design

We need a package design for an up market wine brand named, Brimlow. It will be a Cabernet Sauvignon from the Oakville AVA of Napa Valley. We are looking for a stylish modern label that will stand out on a retail shelf. We want the label to be attention grabbing and stylish while presenting an up market luxury brand.
Updates

Sick

Requirements
Must have
• Must have the words(in order of importance)
-Brimlow
-Cabernet Sauvignon
-Oakville
-Napa Valley
-2018

Must be designed for a traditional "Bordeaux" style bottle (Bottle specs in uploaded files)
Should not have
• Any images of grapes, vineyards, wine glasses or bottles

```html
<!DOCTYPE html>
<html lang="en">
<head>
<meta charset="utf-8">
<title>Brimlow Cabernet Sauvignon – Label</title>
<link rel="stylesheet" href="https://fonts.googleapis.com/css2?family=Playfair+Display:wght@400;700;900&display=swap">
<style>
  :root {
    --backdrop: #1d1d1d;
    --paper: #ebe5db;
    --ink: #1f1f1f;
    --ink-soft: #5a5a5a;
    --red-bright: #e2352c;
    --red-warm: #d8594c;
    --red-deep: #a81f2a;
    --pattern-dark: #231b1c;
  }
  html, body {
    margin: 0;
    padding: 0;
    width: 801px;
    height: 1200px;
    overflow: hidden;
    background: var(--backdrop);
  }
  .label {
    position: absolute;
    left: 156px;
    top: 60px;
    width: 488px;
    height: 1080px;
    background: var(--paper);
    overflow: hidden;
  }
  .label__pattern {
    position: absolute;
    left: 0;
    top: 0;
    width: 100%;
    height: 819px;
    background:
      linear-gradient(180deg,
        rgba(235,229,219,0) 0%,
        rgba(235,229,219,0) 82%,
        rgba(235,229,219,0.55) 100%),
      linear-gradient(135deg,
        var(--red-bright) 0%,
        var(--red-warm) 30%,
        var(--red-deep) 55%,
        var(--pattern-dark) 85%);
  }
  .label__text {
    position: absolute;
    left: 28px;
    right: 28px;
    top: 0;
    font-family: "Playfair Display", Georgia, serif;
    text-transform: uppercase;
    color: var(--ink);
  }
  .brand {
    position: absolute;
    top: 895px;
    margin: 0;
    font-size: 50px;
    font-weight: 900;
    letter-spacing: 4px;
    line-height: 1;
  }
  .varietal, .sub-region, .region, .vintage {
    position: absolute;
    margin: 0;
    line-height: 1;
    white-space: nowrap;
  }
  .varietal { top: 968px; font-size: 19px; font-weight: 700; letter-spacing: 0.5px; }
  .sub-region { top: 994px; font-size: 22px; font-weight: 400; letter-spacing: 2px; color: var(--ink-soft); }
  .region { top: 1020px; font-size: 14px; font-weight: 400; letter-spacing: 1.5px; color: var(--ink-soft); }
  .vintage { top: 1040px; font-size: 21px; font-weight: 700; letter-spacing: 3px; }
</style>
</head>
<body>
  <div class="label">
    <div class="label__pattern" role="img" aria-label="Decorative maze pattern of interlocking red and black diagonal lines, fading to cream at the bottom"></div>
    <div class="label__text">
      <h1 class="brand">Brimlow</h1>
      <p class="varietal">Cabernet Sauvignon</p>
      <p class="sub-region">Oakville</p>
      <p class="region">Napa Valley</p>
      <p class="vintage">2018</p>
    </div>
  </div>
</body>
</html>
```